VORLEN - Business Card Design Project

We need a business card design for a consultant company called VORLEN, LLC. (stands for Vendor Operations Resource Logic Engineering Network). The company provides Information Technology solutions, custom applications, services for financial and supply chain worldwide and focuses on business IT process improvements and all the steps leading to the procurement or integrating of any Enterprise related systems.

Industry/Entity Type

Financial

Requirements
Must have
• - In the submitted proposed version you should have one variant with black background and one with white.
The designer should show the shadow element of the company name in binary code (010101100100111101010010010011000100010101001110). It can be in one line or split in two

In your example please use the following info
Derek Holloway
Principal Consultant
dholloway@vorlenmail.net
+1 (000) 000 - 0000

Please keep in mind that the design should have some spaces to add the second phone and/or web site name
Nice to have
• Since this IT company and is working closely with Accounting and Logistics Application you can add some elements (contour only) of these types of the bussines as well (for example some $ or euro sign or truck or warehouse element)
Should not have
• Don’t use any extra color that is not in the company color logo pattern

```html
<!DOCTYPE html>
<html lang="en">
<head>
<meta charset="utf-8">
<title>VORLEN Business Cards</title>
<link rel="stylesheet" href="https://fonts.googleapis.com/css2?family=Open+Sans:wght@300;400;700&display=swap">
<style>
  :root {
    --page: #d6d6d6;
    --black: #030303;
    --panel: #0e0e0e;
    --white: #ffffff;
    --red: #e8412a;
    --yellow: #fbb416;
    --blue: #1fb0e6;
    --binary-dark: #1c1c1c;
    --binary-light: #ececec;
    --ink: #111111;
  }
  * { margin: 0; padding: 0; box-sizing: border-box; }
  html, body { width: 954px; height: 1200px; overflow: hidden; background: var(--page); }
  body { position: relative; font-family: "Open Sans", Arial, sans-serif; color: var(--white); }

  .card {
    position: absolute;
    left: 77px;
    width: 800px;
    height: 458px;
    border-radius: 30px;
    overflow: hidden;
    box-shadow: 0 6px 14px rgba(0,0,0,0.35);
  }
  .card--front { top: 88px; background: var(--black); --card-bg: var(--black); }
  .card--back { top: 655px; background: var(--white); --card-bg: var(--white); color: var(--ink); }

  .card__swoosh { position: absolute; inset: 0; width: 100%; height: 100%; }

  .card__brand-panel {
    position: absolute;
    left: 26px; top: 25px;
    width: 580px; height: 210px;
    background: var(--panel);
  }

  .brand { position: absolute; }
  .brand__mark {
    position: absolute;
    width: 84px; height: 84px;
    border-radius: 50%;
    background: var(--red);
  }
  .brand__name {
    position: absolute;
    font-weight: 300;
    font-size: 62px;
    line-height: 1;
    letter-spacing: 5px;
    white-space: nowrap;
  }
  .brand__tagline {
    position: absolute;
    font-weight: 700;
    font-size: 12.5px;
    white-space: nowrap;
  }

  .card--front .brand__name,
  .card--front .brand__tagline { color: var(--white); }
  .card--back .brand__name,
  .card--back .brand__tagline { color: var(--ink); }

  .card--front .brand__mark { left: 62px; top: 88px; }
  .card--front .brand__name { left: 196px; top: 98px; }
  .card--front .brand__tagline { left: 198px; top: 155px; }

  .card--back .brand__mark { left: 57px; top: 86px; background: var(--blue); }
  .card--back .brand__name { left: 189px; top: 92px; }
  .card--back .brand__tagline { left: 191px; top: 149px; }

  .contact__name {
    position: absolute;
    left: 55px; top: 258px;
    white-space: nowrap;
    font-size: 22px;
  }
  .contact__name strong { color: var(--red); font-weight: 700; font-size: 32px; }
  .contact__lines {
    position: absolute;
    left: 55px; top: 360px;
    font-size: 18.5px;
    line-height: 34px;
    white-space: nowrap;
  }

  .card__web {
    position: absolute;
    left: 192px; top: 186px;
    font-size: 24px;
    letter-spacing: 6px;
    color: var(--blue);
  }
  .card__binary {
    position: absolute;
    left: 36px; top: 348px;
    font-weight: 700;
    font-size: 27px;
    line-height: 36px;
    color: var(--binary-light);
    letter-spacing: 0.5px;
  }
</style>
</head>
<body>

<section class="card card--front">
  <svg class="card__swoosh" viewBox="0 0 700 400" preserveAspectRatio="none" aria-hidden="true">
    <path d="M565,0 C655,65 680,230 555,400 L700,400 L700,0 Z" fill="var(--red)"/>
    <path d="M383,400 C515,365 625,285 648,150 C660,255 620,350 540,400 Z" fill="var(--yellow)" stroke="var(--black)" stroke-width="4"/>
  </svg>
  <div class="card__brand-panel"></div>
  <div class="brand">
    <span class="brand__mark"></span>
    <span class="brand__name">VORLEN</span>
    <span class="brand__tagline">Vendor Operations Resource Logic Engineering Network</span>
  </div>
  <p class="contact__name"><strong>Derek Holloway</strong> | Principal Consultant</p>
  <p class="contact__lines">P. +1 (000) 000 - 0000 | P. +1 (000) 000 - 0000<br>W. www.vorlen.com | E. dholloway@vorlenmail.net</p>
</section>

<section class="card card--back">
  <svg class="card__swoosh" viewBox="0 0 700 400" preserveAspectRatio="none" aria-hidden="true">
    <path d="M565,0 C655,65 680,230 555,400 L700,400 L700,0 Z" fill="var(--blue)"/>
    <path d="M383,400 C515,365 625,285 648,150 C660,255 620,350 540,400 Z" fill="var(--yellow)" stroke="var(--white)" stroke-width="4"/>
  </svg>
  <div class="brand">
    <span class="brand__mark"></span>
    <span class="brand__name">VORLEN</span>
    <span class="brand__tagline">Vendor Operations Resource Logic Engineering Network</span>
  </div>
  <p class="card__web">www.vorlen.com</p>
  <p class="card__binary">010101100100111101010010<br>010011000100010101001110</p>
</section>

</body>
</html>
```